Velmora Design

Looking for Velmora banner and square design:
Velmora Banner
W:1600 px H:400 px
Square
120x120

Logo attached.

Description: Data-Driven stock market portfolio management using quantitative analysis.

```html
<!DOCTYPE html>
<html lang="en">
<head>
<meta charset="utf-8">
<title>Velmora Banner and Square</title>
<link rel="stylesheet" href="https://fonts.googleapis.com/css2?family=Barlow:wght@300;400;600;700&display=swap">
<style>
  :root {
    --page: #ffffff;
    --label: #2f2f2f;
    --navy-deep: #062a63;
    --navy: #0a3d8f;
    --blue: #0d4fb0;
    --blue-light: #8fb1e6;
    --button-top: #0b4a9c;
    --button-bottom: #052a5e;
    --white: #ffffff;
    --art-light: #dfe8fb;
    --art-mid: #9fb8ee;
  }
  * { margin: 0; padding: 0; box-sizing: border-box; }
  html, body {
    width: 1200px;
    height: 788px;
    overflow: hidden;
    background: var(--page);
    font-family: "Barlow", Arial, sans-serif;
  }
  .sheet { position: relative; width: 1200px; height: 788px; }
  .size-label {
    position: absolute;
    font-weight: 700;
    font-size: 22px;
    color: var(--label);
    letter-spacing: 0.2px;
  }
  .size-label--banner { left: 67px; top: 143px; }
  .size-label--square { left: 78px; top: 518px; }

  .banner {
    position: absolute;
    left: 67px; top: 199px;
    width: 1067px; height: 267px;
    overflow: hidden;
    background:
      radial-gradient(ellipse 120px 90px at 0% 0%, rgba(200,220,255,0.75), rgba(200,220,255,0) 100%),
      radial-gradient(ellipse 260px 140px at 62% 55%, rgba(60,140,230,0.35), rgba(60,140,230,0) 100%),
      radial-gradient(ellipse 200px 80px at 45% 100%, rgba(90,170,240,0.35), rgba(90,170,240,0) 100%),
      linear-gradient(90deg, var(--blue) 0%, var(--navy) 55%, var(--navy-deep) 100%);
  }
  .banner__art {
    position: absolute;
    left: 120px; top: 4px;
    width: 265px; height: 258px;
    border-radius: 50%;
    background: radial-gradient(circle at 45% 40%, var(--art-light) 0%, var(--art-light) 55%, var(--art-mid) 100%);
  }
  .banner__headline {
    position: absolute;
    left: 499px; top: 38px;
    color: var(--white);
    font-size: 32px;
    line-height: 42px;
  }
  .banner__headline .line { display: block; font-weight: 400; white-space: nowrap; }
  .banner__headline .line--strong { font-weight: 700; }
  .banner__cta {
    position: absolute;
    left: 499px; top: 189px;
    width: 185px; height: 39px;
    border-radius: 20px;
    background: linear-gradient(180deg, var(--button-top), var(--button-bottom));
    color: var(--white);
    font-weight: 600;
    font-size: 19px;
    letter-spacing: 0.3px;
    display: flex; align-items: center; justify-content: center;
    padding-right: 10px;
  }

  .square {
    position: absolute;
    top: 561px;
    width: 80px; height: 80px;
    overflow: hidden;
    background:
      radial-gradient(ellipse 60px 40px at 50% 100%, rgba(70,150,230,0.45), rgba(70,150,230,0) 100%),
      linear-gradient(160deg, var(--navy) 0%, var(--navy-deep) 100%);
    color: var(--white);
  }
  .square--text { left: 78px; }
  .square--brand { left: 181px; display: flex; align-items: center; justify-content: center; gap: 4px; }
  .square__copy {
    position: absolute;
    left: 9px; top: 13px;
    font-size: 7.3px;
    line-height: 9.7px;
  }
  .square__copy .line { display: block; white-space: nowrap; }
  .square__copy .line--strong { font-weight: 700; }
  .brand-dot { width: 8px; height: 8px; border-radius: 50%; background: var(--white); }
  .brand-name { font-weight: 700; font-size: 15px; }
</style>
</head>
<body>
<div class="sheet">
  <div class="size-label size-label--banner">1600x400</div>

  <section class="banner">
    <div class="banner__art" role="img" aria-label="Illustration of two people reviewing charts and dashboards on a large screen"></div>
    <h1 class="banner__headline">
      <span class="line">Data-Driven Stock Market</span>
      <span class="line">Portfolio Management</span>
      <span class="line line--strong">Using quantitative analysis</span>
    </h1>
    <div class="banner__cta">GET STARTED</div>
  </section>

  <div class="size-label size-label--square">120x120</div>

  <div class="square square--text">
    <p class="square__copy">
      <span class="line">Data-Driven Stock</span>
      <span class="line">Market Portfolio</span>
      <span class="line">Management</span>
      <span class="line line--strong">Using quantitative</span>
      <span class="line line--strong">analysis</span>
    </p>
  </div>

  <div class="square square--brand">
    <span class="brand-dot"></span>
    <span class="brand-name">Velmora</span>
  </div>
</div>
</body>
</html>
```